Business Card Design Project : Tidewell Press

In preparation for market launch, Whistler's Tidewell Press require the development of a business card. Tidewell Press is a Community online publishing web portal. We provide the the city of Whistler located in B.C. (Canada) business directories, News, Classified ads, News, Events and blogs etc.

The main focus of the brand is to help local businesses to corporate with their online advertisement and marketing. Meeting our clients face to face is a must (B2B).

Target Market(s)

The target market is B2B customers. Business Owners to Marketing, advertising Managers

Industry/Entity Type

Business

Requirements
Must have
• - The business card will be two sided.
the BACK side will have our logo which consist of (icon, url,slogan) submited. The logo will be middle and centred.

The FRONT side should have company details:

Company Legal Name: FERNDALE TIDEWELL PRESS

Owen Marsk
Director of Sales & Marketing

www.ferndaletidewell.biz
owen@ferndaletidewell.biz

Phone: 555 014 3826
#2817 - 562 E. Harlow Ave.
Vancouver, B.C. K7P2R4 Canada
Nice to have
• - For the "FRONT" side of our business card. You can separate or re-arrange with our logo components (icon, logo,slogan). It does not have to be together.

Also our company legal name is rather long so arrange or organize the name in a way to make it shorter. Your experience and creativity will have to come in play.
Should not have
• should not have other colors beside logo color and black text (2 colors). Also nothing Three dimensional

```html
<!DOCTYPE html>
<html lang="en">
<head>
<meta charset="utf-8">
<title>Tidewell Press – Business Card</title>
<link href="https://fonts.googleapis.com/css2?family=Open+Sans:wght@400;600;700&family=Jost:ital,wght@0,400;0,500;1,400&display=swap" rel="stylesheet">
<style>
  :root {
    --brand-blue: #1c72c7;
    --back-blue: #1f7fd0;
    --ink: #111418;
    --muted: #5d6168;
    --paper: #f7f7f6;
    --band: #cfdeee;
    --tab: #d3d5d8;
    --stage: #e4e5e6;
  }
  * { box-sizing: border-box; margin: 0; padding: 0; }
  html, body { width: 1200px; height: 914px; overflow: hidden; }
  body {
    background: var(--stage);
    font-family: "Jost", sans-serif;
    display: flex;
    flex-direction: column;
    align-items: center;
    justify-content: center;
    gap: 64px;
  }
  .card {
    width: 580px;
    height: 332px;
    position: relative;
    overflow: hidden;
  }

  /* Front */
  .card-front { background: var(--paper); }
  .holder { position: absolute; left: 0; top: 28px; display: flex; }
  .holder-tab { width: 22px; height: 40px; background: var(--tab); margin-right: 12px; }
  .holder-name {
    color: var(--brand-blue);
    font-size: 22px;
    font-weight: 500;
    line-height: 1.1;
  }
  .holder-title {
    color: var(--muted);
    font-size: 14px;
    font-style: italic;
    margin-top: 4px;
  }
  .identity {
    position: absolute;
    left: 0; right: 0; top: 104px;
    text-align: center;
    font-family: "Open Sans", sans-serif;
  }
  .brand-name {
    display: inline-flex;
    align-items: center;
    gap: 10px;
    color: var(--brand-blue);
    font-weight: 700;
    font-size: 24px;
    margin-bottom: 6px;
  }
  .brand-dot { width: 14px; height: 14px; border-radius: 50%; background: var(--brand-blue); }
  .url { color: var(--ink); font-weight: 700; font-size: 25px; letter-spacing: -0.3px; line-height: 1.1; }
  .slogan { color: var(--brand-blue); font-weight: 600; font-size: 19px; line-height: 1.15; }
  .contacts {
    position: absolute;
    left: 30px; right: 30px; bottom: 44px;
    display: flex;
    font-size: 13px;
    color: var(--muted);
  }
  .contact-col { display: flex; flex-direction: column; gap: 6px; }
  .contact-col.address { padding-right: 22px; border-right: 1px solid #c9ccd0; }
  .contact-col.reach { padding-left: 22px; }
  .line { display: flex; align-items: flex-start; gap: 8px; }
  .line svg { width: 12px; height: 12px; flex: none; margin-top: 3px; fill: var(--brand-blue); }
  .indent { padding-left: 20px; }
  .band { position: absolute; left: 0; right: 0; bottom: 0; height: 22px; background: var(--band); }

  /* Back */
  .card-back {
    background: var(--back-blue);
    display: flex;
    flex-direction: column;
    align-items: center;
    justify-content: center;
    color: #fff;
    font-family: "Open Sans", sans-serif;
  }
  .card-back .brand-name { color: #fff; font-size: 26px; margin-bottom: 8px; }
  .card-back .brand-dot { background: #fff; }
  .back-slogan { font-size: 19px; font-weight: 400; }
</style>
</head>
<body>
  <section class="card card-front" aria-label="Front of business card">
    <div class="holder">
      <div class="holder-tab"></div>
      <div>
        <div class="holder-name">Owen Marsk</div>
        <div class="holder-title">Director of Sales &amp; Marketing</div>
      </div>
    </div>

    <div class="identity">
      <div class="brand-name"><span class="brand-dot"></span>Tidewell Press</div>
      <div class="url">www.ferndaletidewell.biz</div>
      <div class="slogan">Your information gateway</div>
    </div>

    <div class="contacts">
      <div class="contact-col address">
        <div class="line">
          <svg viewBox="0 0 12 12" aria-hidden="true"><path d="M6 0 L12 5.5 H10 V12 H7.3 V8 H4.7 V12 H2 V5.5 H0 Z"/></svg>
          <span>#2817 - 562 E. Harlow Ave.</span>
        </div>
        <div class="indent">Vancouver, B.C. K7P2R4 Canada</div>
      </div>
      <div class="contact-col reach">
        <div class="line">
          <svg viewBox="0 0 12 12" aria-hidden="true"><path d="M2.4 0.5 L4.4 0.5 L5.2 3.2 L3.8 4.4 C4.5 6 6 7.5 7.6 8.2 L8.8 6.8 L11.5 7.6 L11.5 9.6 C11.5 10.6 10.6 11.5 9.6 11.5 C4.6 11.2 0.8 7.4 0.5 2.4 C0.5 1.4 1.4 0.5 2.4 0.5 Z"/></svg>
          <span>555 014 3826</span>
        </div>
        <div class="line">
          <svg viewBox="0 0 12 12" aria-hidden="true"><path d="M0 2 H12 V3 L6 6.8 L0 3 Z M0 4.3 L6 8.1 L12 4.3 V10.5 H0 Z"/></svg>
          <span>owen@ferndaletidewell.biz</span>
        </div>
      </div>
    </div>

    <div class="band"></div>
  </section>

  <section class="card card-back" aria-label="Back of business card">
    <div class="brand-name"><span class="brand-dot"></span>Tidewell Press</div>
    <div class="back-slogan">Your information gateway</div>
  </section>
</body>
</html>
```